Assessment Service for Aged Care clients information booklet

Our organisation, the Northfield Valley Care Review Bureau, provides in home assessments to aged clients who are seeking assistance with everyday tasks that will support them to remain living in their home. We need a booklet designed to provide to our clients following an aged care assessment for in home services.
Target Market(s)
Aged people living in the community
Colors
Designer to choose colors to be used in the design.
Requirements
Must have
- The booklet must have large print (minimum 12 font size) and be easy to read by the aging consumer. Should be A4 sized. As the content changes from time to time, we need the ability to edit the text. Photos of independent seniors
Nice to have
- reflect the interests of community living seniors
Should not have
- Bright colours that make it difficult to read. Background art under text. Commonwealth Government Logo. Photos of frail aged people (no wheelchairs, carers, anything that make a person look dependent)

```html
<!DOCTYPE html>
<html lang="en">
<head>
<meta charset="utf-8">
<title>Northfield Valley Care Review Bureau – Client Booklet</title>
<link rel="stylesheet" href="https://fonts.googleapis.com/css2?family=Raleway:wght@400;500;600;700;800&family=Yanone+Kaffeesatz:wght@700&display=swap">
<style>
:root{
  --blue:#0a6b9e;
  --blue-dark:#07557f;
  --teal:#5bbdb4;
  --teal-light:#9fd9d2;
  --ink:#5b6670;
  --ink-dark:#33414c;
  --title:#1a6f92;
  --row:#5d6b78;
  --paper-top:#ffffff;
  --paper-bottom:#e7e9ea;
  --board:#8a8b8d;
}
*{box-sizing:border-box;margin:0;padding:0}
html,body{width:1200px;height:1134px;overflow:hidden}
body{background:radial-gradient(ellipse at 50% 45%,#b4b5b7 0%,#8f9092 55%,#6f7072 100%);font-family:'Raleway',sans-serif;position:relative}
.label{position:absolute;font-family:'Yanone Kaffeesatz',sans-serif;font-weight:700;font-size:27px;color:#fff;text-align:center;width:341px;text-shadow:0 1px 2px rgba(0,0,0,.35)}
.page{position:absolute;width:341px;height:483px;background:linear-gradient(var(--paper-top),var(--paper-bottom));box-shadow:0 3px 10px rgba(0,0,0,.35);overflow:hidden;color:var(--ink)}
.page > *{position:absolute}
.band{left:0;top:17px;width:341px;height:20px}
.band-name{font-size:12px;color:var(--teal);font-weight:500;top:19px}
.pgnum{left:0;bottom:12px;width:341px;height:14px}
.h{color:var(--title);font-weight:600;font-size:11.5px;white-space:nowrap}
.h.light{color:#fff}
.rule{height:1px;background:var(--title);opacity:.6}
.txt{font-size:6.2px;line-height:1.45;color:var(--ink)}
.txt.white{color:#eef6fa}
.txt b{color:var(--ink-dark)}
.list{list-style:none;font-size:5.6px;line-height:1.7}
.list li::before{content:"• "}
.panel{background:linear-gradient(160deg,var(--blue-dark),var(--blue))}
.photo{background:linear-gradient(135deg,#b7d3e3,#e9d9c8 55%,#c9b19a)}
/* contents */
.toc{left:22px;top:88px;width:296px;font-size:8.4px;line-height:13.8px;list-style:none;color:var(--ink)}
.toc li{display:flex}
.toc .dots{flex:1;border-bottom:1px dotted #999;margin:0 3px 4px}
.toc .n{color:var(--blue);font-weight:700}
.outlets{left:21px;top:305px;width:298px;border-collapse:collapse;font-size:8.2px}
.outlets th{background:var(--blue);color:#fff;text-align:left;font-size:10px;padding:3px 7px;font-weight:700}
.outlets td{padding:1.6px 7px;height:13.8px}
.outlets td.mail{font-size:5.6px}
.outlets tr.alt td{background:var(--row);color:#fff}
/* cover */
.cover-small{left:22px;top:326px;font-size:16px;font-weight:600;color:#4a5560;letter-spacing:.3px}
.cover-big{left:22px;top:351px;font-size:38px;font-weight:800;color:var(--title);letter-spacing:.5px;line-height:1}
.cover-mid{left:22px;top:396px;font-size:20.5px;font-weight:700;color:var(--title);letter-spacing:.5px}
</style>
</head>
<body>

<div class="label" style="left:65px;top:30px">Cover page</div>
<div class="label" style="left:420px;top:30px">Inner Page 1</div>
<div class="label" style="left:790px;top:30px">Inner Page 2</div>
<div class="label" style="left:65px;top:1066px">Inner Page 3</div>
<div class="label" style="left:420px;top:1064px">Inner Page 4</div>
<div class="label" style="left:790px;top:1064px">Inner Page 5</div>

<!-- Cover -->
<section class="page cover" style="left:65px;top:79px">
  <svg style="left:0;top:0" width="341" height="320" viewBox="0 0 341 320">
    <circle cx="180" cy="150" r="128" fill="none" stroke="#c9cfd2" stroke-width=".6" stroke-dasharray="1.5 2"/>
    <path d="M180 18 A132 132 0 0 1 180 282 A120 120 0 0 0 180 18Z" fill="var(--teal)"/>
    <path d="M262 60 A120 120 0 0 1 200 270 A110 110 0 0 0 262 60Z" fill="var(--blue)"/>
    <circle cx="170" cy="148" r="104" fill="#fff"/>
    <circle cx="24" cy="147" r="13" fill="var(--teal)"/>
    <circle cx="31" cy="178" r="8" fill="var(--teal-light)"/>
    <circle cx="46" cy="199" r="4" fill="var(--teal-light)"/>
  </svg>
  <div class="photo" role="img" aria-label="Photo of a smiling senior couple in warm winter hats outdoors" style="left:63px;top:44px;width:198px;height:198px;border-radius:50%"></div>
  <div class="cover-small">NORTHFIELD VALLEY</div>
  <div style="left:22px;top:350px;width:320px;height:1px;background:#9aa5ad"></div>
  <div class="cover-big">CARE REVIEW</div>
  <div class="cover-mid">BUREAU</div>
</section>

<!-- Inner Page 1 -->
<section class="page" style="left:420px;top:79px">
  <svg class="band" viewBox="0 0 341 20"><rect width="341" height="20" fill="var(--blue)"/><polygon points="228,0 341,0 341,20 220,20" fill="#eef1f2"/></svg>
  <div class="band-name" style="left:242px">Senior Care Link</div>
  <div class="h" style="left:21px;top:52px;font-size:23px;font-weight:700">Contents</div>
  <div class="rule" style="left:130px;top:71px;width:188px"></div>
  <ul class="toc">
    <li>Home Support Assessment<span class="dots"></span><span class="n">3</span></li>
    <li>What happens at a Home Support Assessment?<span class="dots"></span><span class="n">3</span></li>
    <li>After a Home Support Assessment<span class="dots"></span><span class="n">4</span></li>
    <li>Your privacy<span class="dots"></span><span class="n">4</span></li>
    <li>Access to the Senior Care Link Client Portal<span class="dots"></span><span class="n">4</span></li>
    <li>Your rights and responsibilities<span class="dots"></span><span class="n">5</span></li>
    <li>Valley Review Outlet responsibilities<span class="dots"></span><span class="n">5</span></li>
    <li>Complaints and Feedback<span class="dots"></span><span class="n">6</span></li>
    <li>Things to know about your feedback<span class="dots"></span><span class="n">6</span></li>
    <li>How to lodge a complaint or provide feedback<span class="dots"></span><span class="n">7</span></li>
    <li>Who to contact if your needs change<span class="dots"></span><span class="n">7</span></li>
    <li>Other helpful resources<span class="dots"></span><span class="n">8</span></li>
    <li>Information and contacts<span class="dots"></span><span class="n">9</span></li>
  </ul>
  <div class="h" style="left:24px;top:280px;font-size:10.5px;color:var(--blue-dark)">Northfield Valley Care Review Bureau Outlets</div>
  <table class="outlets">
    <tr><th>Outlet</th><th>Phone</th><th>Email</th></tr>
    <tr><td>Ashgrove</td><td>9100 2201</td><td class="mail">intake@ashgrove.example.org</td></tr>
    <tr class="alt"><td>Kestrel Bay</td><td>9100 2202</td><td class="mail">intake@kestrelbay.example.org</td></tr>
    <tr><td>Millbrook</td><td>9100 2203</td><td class="mail"></td></tr>
    <tr class="alt"><td>Hollin care</td><td>9100 2204</td><td class="mail"></td></tr>
    <tr><td>Riverton</td><td>9100 2205</td><td class="mail">review@riverton.example.org</td></tr>
    <tr class="alt"><td>Elmwood</td><td>9100 2206</td><td class="mail"></td></tr>
    <tr><td>Fernhill</td><td>9100 2207</td><td class="mail">care@fernhill.example.org</td></tr>
    <tr class="alt"><td>Oakridge</td><td>9100 2208</td><td class="mail">intake@oakridge.example.org</td></tr>
  </table>
  <svg class="pgnum" viewBox="0 0 341 14"><line x1="0" y1="7" x2="341" y2="7" stroke="#c6cbce"/><circle cx="162" cy="7" r="6.5" fill="#5d6b78" stroke="#fff"/><text x="162" y="9.6" font-size="7.5" fill="#fff" text-anchor="middle" font-family="Raleway,sans-serif">1</text></svg>
</section>

<!-- Inner Page 2 -->
<section class="page" style="left:790px;top:79px">
  <svg class="band" viewBox="0 0 341 20"><rect width="341" height="20" fill="var(--blue)"/><polygon points="0,0 114,0 122,20 0,20" fill="#eef1f2"/></svg>
  <div class="band-name" style="left:14px">Senior Care Link</div>
  <div class="photo" role="img" aria-label="Photo of a happy active senior couple outdoors" style="left:196px;top:38px;width:145px;height:150px;background:linear-gradient(120deg,#ffffff 0%,#dfeaf2 35%,#e6cdb5 70%,#b9c9d6)"></div>
  <div class="h" style="left:21px;top:54px">Home Support Assessment</div>
  <div class="rule" style="left:172px;top:63px;width:52px"></div>
  <p class="txt" style="left:21px;top:72px;width:176px;font-size:5.6px">The Valley Regional Review Service is funded by the National Government and is managed locally by the State Government. Home Support Assessors work for organisations contracted by the Department of Health &amp; Human Services. They carry out Home Support Assessments on behalf of Senior Care Link.</p>
  <p class="txt" style="left:21px;top:140px;width:176px;font-size:5.6px">Home Support Assessments are available for people over the age of 65 years, who need support to be independent. It is also for people of Aboriginal or Torres Strait Islander descent over the age of 50 years.</p>
  <div class="panel" style="left:0;top:188px;width:341px;height:262px"></div>
  <div class="h light" style="left:21px;top:202px">What happens at a Home Support Assessment?</div>
  <div class="rule" style="left:280px;top:210px;width:40px;background:#fff"></div>
  <div class="txt white" style="left:21px;top:222px;width:300px">
    <p>The assessment will be a face-to-face meeting. Assessment staff work with you to identify services that will help you be more independent at home and in the community. They will help you access these services and/or support your carer.</p><br>
    <p>Assessment staff will work with you to create a support plan. The support plan will identify your strengths and any areas of difficulty. It will highlight your goals, and what you would like to achieve. A plan will help identify the types of support that will best suit you as you work towards achieving your goals.</p><br>
    <p>This support may be provided by services, or may be already available in your community to access. It may be things you can do yourself to meet your goals.</p><br>
    <p>If you need support from a service, a Home Support Assessor will make referrals on your behalf. You can also choose to contact your chosen service provider yourself. In this case, your Home Support Assessor will provide you with a referral code. You will need to discuss service availability with the service provider you contact. You will also need to provide them with the referral code to access the service.</p><br>
    <p>If you have chosen to have referrals sent on your behalf, the service providers contact details will be on the support plan. The service provider will contact you to discuss the start of your service. They may come to visit you in your home to discuss your needs. You may wish to contact the service on the number provided in your support plan.</p>
  </div>
  <svg class="pgnum" viewBox="0 0 341 14"><line x1="0" y1="7" x2="341" y2="7" stroke="#c6cbce"/><circle cx="170" cy="7" r="6.5" fill="#5d6b78" stroke="#fff"/><text x="170" y="9.6" font-size="7.5" fill="#fff" text-anchor="middle" font-family="Raleway,sans-serif">2</text></svg>
</section>

<!-- Inner Page 3 -->
<section class="page" style="left:65px;top:576px">
  <svg class="band" viewBox="0 0 341 20"><rect width="341" height="20" fill="var(--blue)"/><polygon points="228,0 341,0 341,20 220,20" fill="#eef1f2"/></svg>
  <div class="band-name" style="left:242px">Senior Care Link</div>
  <div class="h" style="left:22px;top:44px;font-size:12px">After a Home Support Assessment</div>
  <div class="rule" style="left:225px;top:53px;width:92px"></div>
  <div class="txt" style="left:22px;top:58px;width:297px">
    <p>A copy of your support plan will be sent to you. If you have any questions or concerns with the details of your support plan please contact your assessor. If you feel your needs have changed following your assessment, you may request a review of your support plan by calling your Regional Review Service or <b>Senior Care Link on 1800 555 010.</b></p>
    <p style="margin-top:4px">Advocacy services are available which provide information to clients and their families about their rights and responsibilities when accessing aged care services. Advocacy services are free, confidential and independent <b>ph. 1800 555 020.</b></p>
  </div>
  <div class="h" style="left:22px;top:141px;font-size:12px">Your privacy</div>
  <div class="rule" style="left:95px;top:150px;width:222px"></div>
  <p class="txt" style="left:22px;top:159px;width:297px">No information about you is collected or stored without your consent. Your consent is also needed before we speak to any health professional or person on your behalf and before making any referrals for service. If you wish to access your Client Record please call the Senior Care Link contact centre. A full privacy statement is available on the Senior Care Link website at www.seniorcarelink.example.org</p>
  <div class="h" style="left:22px;top:206px;font-size:12px">Access to the Senior Care Link Client Portal</div>
  <div class="rule" style="left:265px;top:215px;width:52px"></div>
  <p class="txt" style="left:22px;top:229px;width:297px">As an aged care consumer, you have access to the Senior Care Link Client portal available through the myPortal web site. In the portal you can:</p>
  <ul class="list" style="left:22px;top:258px;width:200px">
    <li>view your personal profile</li><li>update your contact details</li><li>view and print reports, letters and forms</li><li>view your relationships, including representatives</li><li>remove your nominated representative(s)</li><li>view your current support and action plans</li><li>view your current aged care approvals</li><li>view the aged care services you are currently receiving</li><li>view your interactions with Senior Care Link</li><li>view and upload attachments such as legal or medical documents.</li>
  </ul>
  <div class="photo" role="img" aria-label="Photo of a smiling senior man leaning on a railing by the sea" style="left:218px;top:296px;width:123px;height:155px;border-radius:18px 0 0 0;background:linear-gradient(160deg,#cfe3ef,#8fb5cf 50%,#3e5f86)"></div>
  <svg style="left:200px;top:277px" width="52" height="58" viewBox="0 0 52 58"><path d="M0 0 H34 Q52 0 52 18 V58 H18 Q0 58 0 40Z" fill="var(--teal)"/></svg>
  <div class="panel" style="left:0;top:372px;width:212px;height:78px;background:var(--blue-dark)"></div>
  <div style="left:20px;top:380px;width:185px;font-size:6.2px;line-height:1.4;color:#fff;font-weight:700">
    <p>To log into the client portal or view the Senior Care Link Client Portal user guide, go to: www.seniorcarelink.example.org/portal-login</p>
    <p style="margin-top:5px">If you do not have access to the internet you can call Senior Care Link on 1800 555 010 to update and access information about you on Senior Care Link.</p>
  </div>
  <svg class="pgnum" viewBox="0 0 341 14"><line x1="0" y1="7" x2="341" y2="7" stroke="#c6cbce"/><circle cx="170" cy="7" r="6.5" fill="#5d6b78" stroke="#fff"/><text x="170" y="9.6" font-size="7.5" fill="#fff" text-anchor="middle" font-family="Raleway,sans-serif">3</text></svg>
</section>

<!-- Inner Page 4 -->
<section class="page" style="left:420px;top:576px">
  <svg class="band" viewBox="0 0 341 20"><rect width="341" height="20" fill="var(--blue)"/><polygon points="0,0 114,0 122,20 0,20" fill="#eef1f2"/></svg>
  <div class="band-name" style="left:14px">Senior Care Link</div>
  <div class="h" style="left:21px;top:54px">Your rights and responsibilities</div>
  <div class="rule" style="left:188px;top:63px;width:44px"></div>
  <p class="txt" style="left:21px;top:70px;width:300px;font-size:5.6px">The Home Support Assessment service promotes, and is respectful of, the rights of people that receive their services.</p>
  <p class="txt" style="left:21px;top:88px;font-weight:700;font-size:5.8px;color:var(--ink-dark)">People receiving assessment services by a Valley Review Outlet have:</p>
  <ul class="list" style="left:21px;top:99px;width:300px;font-size:5.1px;line-height:1.55">
    <li>the right to respect for individual human worth and dignity</li><li>right to be treated with courtesy</li><li>the right to be assessed for access to services without discrimination</li><li>the right to be informed and consulted about all services known to the Review Outlet and other relevant matters</li><li>the right to be part of decisions made about their care</li><li>the right to choose from available alternatives</li><li>the right to pursue any complaint about service provision without retribution</li><li>the right to involve an advocate of their choice</li><li>the right to receive a high-quality assessment service</li><li>the right to privacy and confidentiality</li><li>the right to access information kept about themselves through appropriate channels.</li>
  </ul>
  <p class="txt" style="left:21px;top:200px;font-weight:700;font-size:5.8px;color:var(--ink-dark)">People receiving Assessment services by a Valley Review Outlet have a responsibility:</p>
  <ul class="list" style="left:21px;top:211px;width:300px;font-size:5.1px;line-height:1.55">
    <li>to respect the human worth and dignity of Regional Review Service staff</li><li>to treat Regional Review Service staff with courtesy for the results of any decisions they make</li><li>to provide a safe work environment for Regional Review Service staff.</li>
  </ul>
  <svg style="left:0;top:250px" width="341" height="200" viewBox="0 0 341 200"><polygon points="0,6 341,0 341,200 0,200" fill="var(--blue)"/><polygon points="0,0 200,0 208,10 0,10" fill="var(--teal-light)"/><polygon points="150,185 341,178 341,200 160,200" fill="var(--teal)"/></svg>
  <div class="h light" style="left:21px;top:271px">Valley Review Outlet responsibilities</div>
  <div class="rule" style="left:222px;top:280px;width:98px;background:#fff"></div>
  <p style="left:21px;top:293px;width:300px;font-size:6.4px;font-weight:700;color:#fff;line-height:1.35">In providing Home Support Assessment services, Valley Review Outlets have a responsibility:</p>
  <ul class="list" style="left:21px;top:318px;width:305px;font-size:5.2px;line-height:1.95;color:#eef6fa">
    <li>to respect the independence and dignity of the home support assessment recipient</li><li>to ensure that the service recipient's access to an assessment is decided only on the basis of need</li><li>to inform service recipients about options for support in line with their goals, needs and eligibility</li><li>to inform service recipients of their rights and responsibilities in relation to Home Support Assessment</li><li>to be responsive to the diverse social, cultural and physical experiences and needs of service recipients</li><li>to inform consumers of potential fees that they may be expected to pay for services</li><li>to respect the privacy and confidentiality of the service recipient</li><li>to allow the service recipient access to information held by the funded organisation</li><li>to deliver home support assessment services to the consumer in a safe manner</li><li>to recognise the role of carers and be responsive to their need for support</li>
  </ul>
  <svg class="pgnum" viewBox="0 0 341 14"><line x1="0" y1="7" x2="341" y2="7" stroke="#c6cbce"/><circle cx="170" cy="7" r="6.5" fill="#5d6b78" stroke="#fff"/><text x="170" y="9.6" font-size="7.5" fill="#fff" text-anchor="middle" font-family="Raleway,sans-serif">4</text></svg>
</section>

<!-- Inner Page 5 -->
<section class="page" style="left:790px;top:576px">
  <svg style="left:0;top:0" width="341" height="210" viewBox="0 0 341 210"><rect width="341" height="185" fill="var(--blue)"/><rect y="17" width="341" height="20" fill="var(--blue-dark)"/><polygon points="228,17 341,17 341,37 220,37" fill="#eef1f2"/><polygon points="0,37 160,37 170,48 0,48" fill="#f0f2f3"/><polygon points="170,172 341,170 341,192 160,192" fill="var(--teal)"/></svg>
  <div class="band-name" style="left:242px">Senior Care Link</div>
  <ul class="list" style="left:20px;top:56px;width:305px;font-size:5.2px;line-height:1.5;color:#eef6fa">
    <li>to allow the carer access to information held by the provider about the service recipient where the carer is the legal guardian or has been so authorised by the service recipient</li>
    <li style="margin-top:6px">to respect a service recipient's refusal of a service and to ensure any future attempt by the service recipient to access assessment services is not prejudiced because of that refusal</li>
    <li style="margin-top:6px">to accept the service recipient's choice and involvement of an advocate to represent his or her interests</li>
    <li style="margin-top:6px">to deal with service recipient's complaints fairly and promptly and without retribution</li>
    <li style="margin-top:6px">to mediate and attempt to negotiate a solution if conflict arises between the carer and the older person</li>
    <li style="margin-top:10px">to ensure that the service recipient continues to receive services agreed with the provider, taking the service recipient's changing needs into account</li>
  </ul>
  <div class="h" style="left:21px;top:204px">Complaints and Feedback</div>
  <div class="rule" style="left:166px;top:213px;width:155px"></div>
  <div class="txt" style="left:21px;top:223px;width:300px;font-size:5.8px">
    <p>Northfield Valley Bureau aim to provide a quality assessment service. We welcome your feedback to help us improve our services to you.</p>
    <p style="margin-top:6px">Feedback provided is treated confidentially and addressed in a fair and just manner. We investigate all concerns raised and will respond within five business days of receipt. Making a complaint and expressing a concern will not result in a negative impact on the service you receive.</p>
  </div>
  <p style="left:21px;top:291px;font-size:6.6px;font-weight:700;color:var(--ink-dark)">Things to know about your feedback</p>
  <ul class="list" style="left:21px;top:313px;width:300px;font-size:5.2px;line-height:1.95">
    <li>You have the right to provide feedback and to have your concern investigated objectively.</li><li>Your concern will be taken seriously and followed up.</li><li>Your feedback will not impact on the service you receive.</li><li>You do not have to supply your details, however please do so if you want us to contact you in relation to your feedback.</li><li>You are encouraged to raise issues as early as possible to clear up misunderstandings and to resolve issues early.</li><li>We greatly appreciate hearing about a positive experience you have had with our service.</li><li>Please contact us if you need someone to communicate or advocate on your behalf. You can also contact the Aged Care advocacy service <b>1800 555 020.</b></li>
  </ul>
  <svg style="left:0;top:434px" width="341" height="18" viewBox="0 0 341 18"><polygon points="0,0 120,0 110,18 0,18" fill="var(--teal)"/><polygon points="120,0 341,0 341,18 110,18" fill="var(--blue)"/></svg>
  <svg class="pgnum" viewBox="0 0 341 14"><line x1="0" y1="7" x2="341" y2="7" stroke="#c6cbce"/><circle cx="170" cy="7" r="6.5" fill="#5d6b78" stroke="#fff"/><text x="170" y="9.6" font-size="7.5" fill="#fff" text-anchor="middle" font-family="Raleway,sans-serif">5</text></svg>
</section>

</body>
</html>
```